Cover for Every door Opens Where Every Door Opens

Book Cover Request
Format: Print and electronic (Quillmart)
Book Title: Every Door Opens Where Every Door Opens: Practical Roadmap for Courage and Progress
Author: R.K. Vantreel
Description: This self-help book, written by me, a self-proclaimed nobody, is filled with actionable insights and proven strategies that can help anyone. It combines humor with a serious undertone to deliver practical advice without the typical "self-helpy" vibe.
Catchphrase for the Cover: "Go from Oh Shit to Crushing It!" (or something similar)
Style: I want the cover to reflect my personality—funny, yet serious when needed. I'm open to suggestions and would love to see a design that captures the essence of the book without being too typical of the self-help genre.
Additional Information: I've attached a rough draft of the Quillmart description for more context.
Thank you for your help!
Target Market(s)
Anyone. but id say over 25
Requirements
Nice to have
- Honestly im really at a loss. Im hoping the description will help guide you. I gues i would like it to satand out of course. Be diffrent....but i know how crazy that sounds because everyone wants that. Just give me soem ideas!

```html
<!DOCTYPE html>
<html lang="en">
<head>
<meta charset="utf-8">
<title>Every door Opens Where Every Door Opens — Cover</title>
<link rel="stylesheet" href="https://fonts.googleapis.com/css2?family=Red+Hat+Display:ital,wght@0,800;0,900;1,500&family=Nunito+Sans:wght@300;400&display=swap">
<style>
  :root {
    --backdrop: #8e898b;
    --paper: #dcdcdc;
    --title-grey: #8a8a8a;
    --title-red: #c4161c;
    --ink: #2b2b2b;
    --art-light: #d6d6d6;
    --art-mid: #c4c4c4;
  }
  html, body {
    margin: 0;
    padding: 0;
    width: 1200px;
    height: 900px;
    overflow: hidden;
    background: var(--backdrop);
  }
  .canvas {
    width: 1200px;
    height: 900px;
    display: flex;
    align-items: center;
    justify-content: center;
  }
  .cover {
    position: relative;
    width: 570px;
    height: 810px;
    background: var(--paper);
    overflow: hidden;
  }
  .title-block {
    position: absolute;
    left: 42px;
    top: 40px;
    right: 20px;
  }
  .title-line {
    margin: 0;
    font-family: "Red Hat Display", sans-serif;
    font-size: 50px;
    line-height: 0.9;
    letter-spacing: -0.5px;
  }
  .title-lead {
    font-weight: 900;
    color: var(--title-grey);
  }
  .title-join {
    font-weight: 500;
    font-style: italic;
    color: var(--title-grey);
  }
  .title-echo {
    font-weight: 900;
    color: var(--title-red);
  }
  .subtitle {
    margin: 8px 0 0;
    font-family: "Nunito Sans", sans-serif;
    font-weight: 300;
    font-size: 19px;
    letter-spacing: 0.6px;
    color: var(--ink);
  }
  .emblem-art {
    position: absolute;
    left: 115px;
    top: 270px;
    width: 400px;
    height: 380px;
    border-radius: 50%;
    background: radial-gradient(circle at 60% 58%, var(--art-mid) 0%, var(--art-light) 55%, var(--paper) 72%);
  }
  .author {
    position: absolute;
    left: 0;
    right: 0;
    bottom: 70px;
    padding-left: 150px;
    text-align: center;
    font-family: "Red Hat Display", sans-serif;
    font-weight: 800;
    font-size: 22px;
    letter-spacing: 0.5px;
    color: var(--ink);
  }
</style>
</head>
<body>
  <main class="canvas">
    <article class="cover">
      <header class="title-block">
        <h1 class="title-line title-lead">Every door Opens</h1>
        <p class="title-line title-join">Where</p>
        <p class="title-line title-echo">Every Door Opens</p>
        <p class="subtitle">Practical Roadmap for Courage and Progress</p>
      </header>

      <div class="emblem-art" role="img" aria-label="Line illustration of nested grey rings flowing into one another"></div>

      <p class="author">R.K. Vantreel</p>
    </article>
  </main>
</body>
</html>
```